Looking for a dynamic business card for a pizzeria.

A business card with our food, logo, and space for name, title, email, website, phone. The card should convey quality, unique, amazing. On the front, I envision food photo or photos with the owners names and contact information. On the back, more food with locations, website, facebook, twitter, instagram icons. It should look polished, not cartoonish, or plain.
Target Market(s)
upscale, local food buyers, 30-50 years in age.
Industry/Entity Type
Restaurant
Contact Information for Business Card
Business Name: Crustelli, LLC
Website: www.crustelli-example.com
Back:
2 locations: (can list on the back of card)
1. Harborside
3807 Marlow Street
Alderport, WA 98001
360-555-0143
2. Cedar Ridge
1736 Quenby Street
Alderport, WA 98004
360-555-0187
front:
EDITABLE space for
Business name
Person's Name
title
2nd title
Email address
cell-phone number
Requirements
Must have
- logo
- my food photo or photos (no watermarks showing)
- locations on back
- Person contact information on front
- full bleed

```html
<!DOCTYPE html>
<html lang="en">
<head>
<meta charset="utf-8">
<title>Crustelli Business Card</title>
<link rel="stylesheet" href="https://fonts.googleapis.com/css2?family=Open+Sans:wght@400;600;700&display=swap">
<style>
  :root {
    --bg: #e9e4dc;
    --paper: #f7f7f5;
    --green-dark: #1f5a2a;
    --green: #2f7a3a;
    --green-light: #5e9f66;
    --red: #d3251d;
    --white: #ffffff;
    --text-soft: #e4efe5;
    --social: #3f7fc3;
  }
  * { margin: 0; padding: 0; box-sizing: border-box; }
  html, body { width: 1200px; height: 1062px; overflow: hidden; }
  body {
    background: var(--bg);
    font-family: "Open Sans", Arial, sans-serif;
    position: relative;
  }
  .card {
    position: absolute;
    left: 220px;
    width: 760px;
    height: 434px;
    overflow: hidden;
    box-shadow: 0 6px 18px rgba(0,0,0,0.18);
  }
  /* Front */
  .card-front { top: 50px; background: var(--paper); }
  .front-logo {
    position: absolute; top: 0; left: 0; right: 0; height: 262px;
    display: flex; align-items: center; justify-content: center; gap: 22px;
  }
  .logo-name {
    font-size: 78px; font-weight: 600; color: var(--green);
    letter-spacing: 2px;
  }
  .logo-dot {
    width: 70px; height: 70px; border-radius: 50%; background: var(--red);
  }
  .front-stripe {
    position: absolute; top: 262px; left: 0; right: 0; height: 10px; background: var(--red);
  }
  .front-band {
    position: absolute; top: 272px; left: 0; right: 0; bottom: 0;
    background: linear-gradient(160deg, var(--green) 0%, var(--green-dark) 100%);
    display: flex; justify-content: space-between; align-items: center;
    padding: 0 56px;
  }
  .person-name { font-size: 26px; font-weight: 700; color: var(--white); }
  .person-title { font-size: 20px; color: var(--text-soft); margin-top: 4px; }
  .contact-list { list-style: none; }
  .contact-list li {
    display: flex; align-items: center; gap: 12px;
    font-size: 19px; color: var(--white); line-height: 1.6;
  }
  .contact-list svg { width: 18px; height: 18px; flex: none; }

  /* Back */
  .card-back {
    top: 534px;
    background: radial-gradient(ellipse at 65% 45%, var(--green-light) 0%, var(--green) 45%, var(--green-dark) 100%);
  }
  .food-photo {
    position: absolute; left: 0; top: 0; width: 280px; height: 250px;
    background: radial-gradient(ellipse at 45% 50%, #8fb865 0%, #5f8f3f 45%, rgba(47,122,58,0) 75%);
  }
  .locations {
    position: absolute; left: 300px; top: 34px;
    display: flex; gap: 46px; color: var(--white);
  }
  .location h3 { font-size: 20px; font-weight: 700; margin-bottom: 4px; }
  .location p { font-size: 17px; line-height: 1.45; }
  .location .phone {
    font-weight: 700; display: flex; align-items: center; gap: 8px; margin-top: 4px;
  }
  .location .phone svg { width: 15px; height: 15px; }
  .back-logo {
    position: absolute; left: 56px; bottom: 48px;
    display: flex; align-items: center; gap: 16px;
  }
  .back-logo .logo-name { font-size: 56px; color: var(--white); }
  .back-logo .logo-dot { width: 48px; height: 48px; background: var(--white); }
  .social {
    position: absolute; right: 48px; bottom: 52px; display: flex; gap: 10px;
  }
  .social span { width: 44px; height: 44px; background: var(--social); display: block; }
</style>
</head>
<body>
  <section class="card card-front">
    <div class="front-logo">
      <span class="logo-dot"></span>
      <span class="logo-name">Crustelli</span>
    </div>
    <div class="front-stripe"></div>
    <div class="front-band">
      <div class="person">
        <div class="person-name">Marco Vellani</div>
        <div class="person-title">Manager</div>
      </div>
      <ul class="contact-list">
        <li>
          <svg viewBox="0 0 24 24"><path fill="#fff" d="M6.6 10.8a15.1 15.1 0 0 0 6.6 6.6l2.2-2.2c.3-.3.7-.4 1-.2 1.1.4 2.3.6 3.6.6.6 0 1 .4 1 1V20c0 .6-.4 1-1 1A17 17 0 0 1 3 4c0-.6.4-1 1-1h3.5c.6 0 1 .4 1 1 0 1.3.2 2.5.6 3.6.1.3 0 .7-.2 1z"/></svg>
          360-555-0100
        </li>
        <li>
          <svg viewBox="0 0 24 24" fill="none" stroke="#fff" stroke-width="2"><circle cx="12" cy="12" r="9"/><path d="M3 12h18M12 3c3 3 3 15 0 18M12 3c-3 3-3 15 0 18"/></svg>
          www.crustelli-example.com
        </li>
        <li>
          <svg viewBox="0 0 24 24" fill="none" stroke="#fff" stroke-width="2"><circle cx="12" cy="12" r="4"/><path d="M16 8v5a3 3 0 0 0 6 0v-1a10 10 0 1 0-4 8"/></svg>
          info@crustelli-example.com
        </li>
      </ul>
    </div>
  </section>

  <section class="card card-back">
    <div class="food-photo" role="img" aria-label="Photo of a freshly baked pizza"></div>
    <div class="locations">
      <div class="location">
        <h3>1. Harborside</h3>
        <p>3807 Marlow Street<br>Alderport, WA 98001</p>
        <p class="phone"><svg viewBox="0 0 24 24"><path fill="var(--red)" d="M6.6 10.8a15.1 15.1 0 0 0 6.6 6.6l2.2-2.2c.3-.3.7-.4 1-.2 1.1.4 2.3.6 3.6.6.6 0 1 .4 1 1V20c0 .6-.4 1-1 1A17 17 0 0 1 3 4c0-.6.4-1 1-1h3.5c.6 0 1 .4 1 1 0 1.3.2 2.5.6 3.6.1.3 0 .7-.2 1z"/></svg>360-555-0143</p>
      </div>
      <div class="location">
        <h3>2. Cedar Ridge</h3>
        <p>1736 Quenby Street<br>Alderport, WA 98004</p>
        <p class="phone"><svg viewBox="0 0 24 24"><path fill="var(--red)" d="M6.6 10.8a15.1 15.1 0 0 0 6.6 6.6l2.2-2.2c.3-.3.7-.4 1-.2 1.1.4 2.3.6 3.6.6.6 0 1 .4 1 1V20c0 .6-.4 1-1 1A17 17 0 0 1 3 4c0-.6.4-1 1-1h3.5c.6 0 1 .4 1 1 0 1.3.2 2.5.6 3.6.1.3 0 .7-.2 1z"/></svg>360-555-0187</p>
      </div>
    </div>
    <div class="back-logo">
      <span class="logo-dot"></span>
      <span class="logo-name">Crustelli</span>
    </div>
    <div class="social" aria-label="Social media links">
      <span></span><span></span><span></span>
    </div>
  </section>
</body>
</html>
```